Business Cards

Business card design for my company.
I would like the card's background colour to be black. You can also see our web site to get an idea of our brand. https://www.dlqmarrowfield.com.au/
- Name
- Email

```html
<!DOCTYPE html>
<html lang="en">
<head>
<meta charset="utf-8">
<title>DLQ Marrowfield – Business Card</title>
<link rel="stylesheet" href="https://fonts.googleapis.com/css2?family=Roboto:wght@400;500;700&display=swap">
<style>
  :root {
    --page: #e9e6e1;
    --card-black: #060707;
    --brand-green: #1f9a45;
    --text-white: #f2f2f2;
    --divider: #5a5a5a;
    --photo-tone-a: #6c7584;
    --photo-tone-b: #59645e;
  }
  * { box-sizing: border-box; margin: 0; padding: 0; }
  html, body {
    width: 1200px; height: 900px; overflow: hidden;
    background: var(--page);
    font-family: "Roboto", Arial, sans-serif;
  }
  .sheet {
    width: 1200px; height: 900px;
    display: flex; flex-direction: column; align-items: center; justify-content: center;
    gap: 40px;
  }
  .card {
    position: relative;
    width: 620px; height: 380px;
    border-radius: 34px;
    overflow: hidden;
    box-shadow: 0 10px 30px rgba(0,0,0,.18);
  }

  /* Front */
  .card--front .photo {
    position: absolute; inset: 0;
    background: linear-gradient(160deg, var(--photo-tone-a) 0%, var(--photo-tone-b) 100%);
  }
  .card--front .front-brand {
    position: absolute; left: 46px; top: 196px;
    display: flex; align-items: center; gap: 10px;
    color: var(--text-white);
    font-weight: 700; font-size: 26px; letter-spacing: 1px;
  }

  /* Back */
  .card--back { background: var(--card-black); color: var(--text-white); }
  .brand {
    position: absolute; left: 60px; top: 110px;
    display: flex; align-items: center; gap: 14px;
    font-weight: 700; font-size: 36px; letter-spacing: 1.5px;
    color: var(--text-white);
  }
  .brand-mark { width: 22px; height: 22px; background: var(--brand-green); }
  .front-brand .brand-mark { width: 16px; height: 16px; }

  .person {
    position: absolute; right: 276px; top: 248px;
    text-align: right;
  }
  .person .role { font-size: 15px; font-weight: 400; }
  .person .name {
    font-size: 21px; font-weight: 500; color: var(--brand-green);
    text-transform: uppercase; margin-top: 3px;
  }
  .divider {
    position: absolute; left: 360px; top: 220px;
    width: 1px; height: 110px; background: var(--divider);
  }
  .contacts {
    position: absolute; left: 376px; top: 224px;
    list-style: none;
    font-size: 13px; line-height: 1;
  }
  .contacts li { display: flex; align-items: center; gap: 8px; height: 25px; white-space: nowrap; }
  .contacts svg { width: 14px; height: 14px; flex: none; fill: var(--brand-green); }
  .contacts .accent { color: var(--brand-green); }
</style>
</head>
<body>
<main class="sheet">

  <section class="card card--front" aria-label="Card front">
    <div class="photo" role="img" aria-label="Full-bleed photograph of a completed modern home"></div>
    <div class="front-brand"><span class="brand-mark"></span>DLQ MARROWFIELD</div>
  </section>

  <section class="card card--back" aria-label="Card back">
    <div class="brand"><span class="brand-mark"></span>DLQ MARROWFIELD</div>

    <div class="person">
      <p class="role">General Manager</p>
      <p class="name">Owen Calder</p>
    </div>

    <div class="divider"></div>

    <ul class="contacts">
      <li>
        <svg viewBox="0 0 24 24" aria-hidden="true"><path d="M6.6 10.8a15 15 0 0 0 6.6 6.6l2.2-2.2a1 1 0 0 1 1-.25 11.4 11.4 0 0 0 3.6.57 1 1 0 0 1 1 1V20a1 1 0 0 1-1 1A17 17 0 0 1 3 4a1 1 0 0 1 1-1h3.5a1 1 0 0 1 1 1c0 1.25.2 2.45.57 3.57a1 1 0 0 1-.25 1z"/></svg>
        <span>0400 555 173</span>
      </li>
      <li>
        <svg viewBox="0 0 24 24" aria-hidden="true"><path d="M2 5h20v14H2zm2 2v.5l8 5 8-5V7zm0 2.8V17h16V9.8l-8 5z"/></svg>
        <span>info@<span class="accent">dlqmarrowfield</span>.com.au</span>
      </li>
      <li>
        <svg viewBox="0 0 24 24" aria-hidden="true"><path d="M12 2a10 10 0 1 0 0 20 10 10 0 0 0 0-20zm6.9 6h-3a15 15 0 0 0-1.3-3.9A8 8 0 0 1 18.9 8zM12 4c.8 1.1 1.5 2.5 1.9 4h-3.8c.4-1.5 1.1-2.9 1.9-4zM4.3 14a8 8 0 0 1 0-4h3.4a16 16 0 0 0 0 4zm.8 2h3a15 15 0 0 0 1.3 3.9A8 8 0 0 1 5.1 16zm3-8h-3a8 8 0 0 1 4.3-3.9A15 15 0 0 0 8.1 8zM12 20c-.8-1.1-1.5-2.5-1.9-4h3.8c-.4 1.5-1.1 2.9-1.9 4zm2.3-6H9.7a14 14 0 0 1 0-4h4.6a14 14 0 0 1 0 4zm.3 5.9A15 15 0 0 0 15.9 16h3a8 8 0 0 1-4.3 3.9zM16.3 14a16 16 0 0 0 0-4h3.4a8 8 0 0 1 0 4z"/></svg>
        <span>www.<span class="accent">dlqmarrowfield</span>.com.au</span>
      </li>
      <li>
        <svg viewBox="0 0 24 24" aria-hidden="true"><path d="M12 2a7 7 0 0 0-7 7c0 5.2 7 13 7 13s7-7.8 7-13a7 7 0 0 0-7-7zm0 9.5A2.5 2.5 0 1 1 12 6.5a2.5 2.5 0 0 1 0 5z"/></svg>
        <span>Lindmoor, Tasmania, Australia</span>
      </li>
    </ul>
  </section>

</main>
</body>
</html>
```